Christmas Concert

"The Marlowe Voices" is Ashcombe Manor's professional chamber choir. www.marlowevoicesfolk.com

They are performing a Christmas concert in Oxford's oldest building, St Aldric by the West Bridge (almost 1,000 years old), and the concert will be by candlelight.

We are looking for a dramatic and sophisticated Christmas poster that will stand out in the crowd of other posters in Oxford city centre.

We are thinking of calling the concert "Christmas with the Marlowe Voices" or "Christmas Carols by Candlelight" but we're open to suggestions.

The poster will be used for digital dissemination (as well as Facebook/Twitter) as well as print - A2 (portrait) will be the maximum size.

See attached photo of the ensemble. It would be a good to incorporate this in some way.

Industry/Entity Type

Building

Requirements
Nice to have
• The Marlowe Voices
• Ewan Pritchard-Lowe, Director
• Sunday 8 December
• 8pm
• Tickets £10/£5
• MarloweVoicesFolk.com

```html
<!DOCTYPE html>
<html lang="en">
<head>
<meta charset="utf-8">
<title>Christmas Carols by Candlelight – Marlowe Voices</title>
<link href="https://fonts.googleapis.com/css2?family=Philosopher:ital,wght@0,700;1,700&display=swap" rel="stylesheet">
<style>
  :root {
    --red-deep: #7e060c;
    --red-main: #c3141d;
    --red-bright: #d9262b;
    --title-red: #ad0b12;
    --cream: #fdf3c2;
    --cream-soft: #fbe8b4;
    --peach: #f3b58d;
    --frame: #fbf1c0;
    --photo-stone: #b9b39c;
    --photo-grass: #6f7360;
  }
  * { margin: 0; padding: 0; box-sizing: border-box; }
  html, body { width: 849px; height: 1200px; overflow: hidden; background: var(--red-deep); }
  .poster {
    position: relative;
    width: 849px;
    height: 1200px;
    overflow: hidden;
    font-family: "Philosopher", "Optima", sans-serif;
    font-style: italic;
    font-weight: 700;
    background:
      radial-gradient(ellipse 70% 40% at 45% 22%, var(--red-bright) 0%, var(--red-main) 45%, transparent 100%),
      radial-gradient(ellipse 80% 35% at 35% 90%, var(--red-main) 0%, #a80d15 55%, var(--red-deep) 100%);
  }
  .band { position: absolute; inset: 0; }
  .ensemble-name {
    position: absolute;
    left: 34px;
    top: 88px;
    color: var(--cream);
    font-size: 50px;
    line-height: 46px;
  }
  .ensemble-photo-frame {
    position: absolute;
    left: 360px;
    top: 12px;
    width: 422px;
    height: 244px;
    background: var(--frame);
    padding: 10px 11px 12px 12px;
  }
  .ensemble-photo {
    width: 100%;
    height: 100%;
    background: linear-gradient(180deg, #d8d5c8 0%, var(--photo-stone) 38%, #8c8a78 62%, var(--photo-grass) 100%);
  }
  .concert-title {
    position: absolute;
    left: 34px;
    top: 490px;
    color: var(--title-red);
    font-size: 80px;
    line-height: 1;
  }
  .concert-title span { display: block; }
  .concert-title .line-carols { margin-left: 66px; margin-top: -6px; }
  .concert-title .line-candle { margin-top: 2px; }
  .concert-title .by { font-size: 40px; margin-left: 28px; margin-right: 4px; }
  .details { position: absolute; left: 34px; color: var(--cream); }
  .venue-label { top: 944px; font-size: 21px; }
  .venue-name { top: 966px; font-size: 33px; }
  .venue-note { top: 1005px; left: 80px; font-size: 21px; }
  .date { top: 1066px; font-size: 24px; }
  .time { top: 1092px; left: 66px; font-size: 24px; }
  .website { top: 1152px; font-size: 14px; }
</style>
</head>
<body>
<main class="poster">
  <svg class="band" width="849" height="1200" viewBox="0 0 849 1200" aria-hidden="true">
    <defs>
      <linearGradient id="bandGlow" x1="0" y1="0" x2="1" y2="1">
        <stop offset="0" stop-color="#f6c79c"/>
        <stop offset="0.35" stop-color="#fbe8b4"/>
        <stop offset="0.65" stop-color="#f7d7a5"/>
        <stop offset="1" stop-color="#f0a684"/>
      </linearGradient>
      <radialGradient id="bandLight" cx="0.45" cy="0.55" r="0.6">
        <stop offset="0" stop-color="#fff6d2" stop-opacity="0.8"/>
        <stop offset="1" stop-color="#fff6d2" stop-opacity="0"/>
      </radialGradient>
    </defs>
    <polygon points="0,342 849,256 849,836 0,918" fill="url(#bandGlow)"/>
    <polygon points="0,342 849,256 849,836 0,918" fill="url(#bandLight)"/>
  </svg>

  <h2 class="ensemble-name">Marlowe<br>Voices</h2>

  <div class="ensemble-photo-frame">
    <div class="ensemble-photo" role="img" aria-label="Photograph of the nine members of the choir in concert dress standing in front of a stately stone manor"></div>
  </div>

  <h1 class="concert-title">
    <span>Christmas</span>
    <span class="line-carols">Carols</span>
    <span class="line-candle"><span class="by" style="display:inline">by</span>Candlelight</span>
  </h1>

  <p class="details venue-label">Venue:</p>
  <p class="details venue-name">St Aldric by the West Bridge</p>
  <p class="details venue-note">Oxford's oldest building</p>
  <p class="details date">24 December 2013</p>
  <p class="details time">8pm to 11pm</p>
  <p class="details website">www.marlowevoicesfolk.com</p>
</main>
</body>
</html>
```